Business card for Real Estate Company located in Coastal area of spain

Want a business card design. Simple, professional, horizontal layout. will be 2 sided. Name of company (logo big on front). Name of agent, phone and email address. Back side will be list of general services we provide. Would like to see 2 separate concepts using the 2 separate logo treatments. One using Rich dark, bright blue as the stock color, and the other using White as the stock color.
Logo files uploaded (2 different versions) Domain (harbourkeyestates.com) Moraira-Calpe-Altea-Javea-Denia-Marina Alta Area (perhaps across the bottom of the front of card0 Ingrid Tavel Licensed Estate Agent / Partner Ingrid@harbourkeyestates.com +34.611.48.27.09 Back of card should list services offered

Real Estate Sales and Investments Real Estate Rental Management Kitchen, Bathroom Reformations Complete Home Reformation Services Window and Door Replacement Landscape and Garden Management Pool and Jacuzzi Service

Target Market(s)

Real estate and construction

Industry/Entity Type

Real Estate

Contact Information for Business Card

Logo files uploaded (2 different versions) Domain (harbourkeyestates.com) Moraira-Calpe-Altea-Javea-Denia-Marina Alta Area (perhaps across the bottom of the front of card0 Ingrid Tavel Licensed Estate Agent / Partner Ingrid@harbourkeyestates.com +34.611.48.27.09

Colors

Designer to choose colors to be used in the design.

Requirements
Must have
• progressive look professional
Nice to have
• Front big logo, Agent details. Back, list of services included in project description
Should not have
• Gloss finish for card

```html
<!DOCTYPE html>
<html lang="en">
<head>
<meta charset="utf-8">
<title>Harbourkeyestates – Business Card</title>
<link href="https://fonts.googleapis.com/css2?family=Montserrat:wght@400;500;700&display=swap" rel="stylesheet">
<style>
  :root {
    --stage: #2a2a2a;
    --orchid: #ab6aa9;
    --paper: #ffffff;
    --royal: #4a62b0;
    --violet: #9a5fb0;
    --ink: #3a3a3a;
    --white: #ffffff;
  }
  * { margin: 0; padding: 0; box-sizing: border-box; }
  html, body {
    width: 1200px; height: 900px; overflow: hidden;
    background: var(--stage);
    font-family: "Montserrat", sans-serif;
  }
  .stage {
    width: 1200px; height: 900px;
    display: flex; flex-direction: column; align-items: center; justify-content: center;
    gap: 36px;
  }
  .card {
    position: relative;
    width: 700px; height: 400px;
    overflow: hidden;
  }

  /* Front (services side) */
  .card--services {
    background: var(--orchid);
    color: var(--white);
    display: flex; flex-direction: column; align-items: center; justify-content: center;
    text-align: center;
  }
  .card--services .brand-name {
    font-size: 38px; font-weight: 400; letter-spacing: 0.5px;
    color: var(--white);
  }
  .service-list {
    list-style: none;
    margin-top: 58px;
    font-size: 16px; font-weight: 400; letter-spacing: 0.6px; line-height: 1.6;
  }

  /* Back (contact side) */
  .card--contact { background: var(--paper); }
  .edge-bar {
    position: absolute; width: 16px; background: var(--royal);
  }
  .edge-bar--left { left: 0; top: 80px; height: 185px; }
  .edge-bar--right { right: 0; top: 135px; height: 205px; }

  .brand-block {
    position: absolute; left: 40px; top: 130px; width: 290px;
  }
  .card--contact .brand-name {
    font-size: 22px; font-weight: 400; color: var(--royal);
  }
  .divider {
    position: absolute; left: 340px; top: 110px; width: 1px; height: 140px;
    background: linear-gradient(var(--violet), var(--royal));
  }
  .agent {
    position: absolute; left: 365px; top: 108px;
  }
  .agent-name {
    font-size: 26px; font-weight: 700; letter-spacing: 1px; text-transform: uppercase;
    background: linear-gradient(90deg, var(--royal), var(--violet));
    -webkit-background-clip: text; background-clip: text; color: transparent;
  }
  .agent-title {
    font-size: 14px; font-weight: 400; color: var(--ink); letter-spacing: 0.4px;
    margin-top: 2px;
  }
  .contact-list {
    list-style: none; margin-top: 16px;
    font-size: 14px; color: var(--ink); letter-spacing: 0.4px;
  }
  .contact-list li {
    display: flex; align-items: center; gap: 10px; line-height: 1.75;
  }
  .contact-list svg { width: 13px; height: 13px; fill: var(--royal); flex: none; }
  .area-line {
    position: absolute; left: 0; right: 0; bottom: 58px;
    text-align: center;
    font-size: 16px; color: var(--ink); letter-spacing: 0.5px;
  }
</style>
</head>
<body>
<main class="stage">

  <section class="card card--services" aria-label="Card front: services">
    <p class="brand-name">harbourkeyestates.com</p>
    <ul class="service-list">
      <li>Real Estate Sales and Investments | Rental Management</li>
      <li>Home Reformation Services</li>
    </ul>
  </section>

  <section class="card card--contact" aria-label="Card back: agent contact">
    <span class="edge-bar edge-bar--left"></span>
    <span class="edge-bar edge-bar--right"></span>

    <div class="brand-block">
      <p class="brand-name">harbourkeyestates.com</p>
    </div>

    <span class="divider"></span>

    <div class="agent">
      <h1 class="agent-name">Ingrid Tavel</h1>
      <p class="agent-title">Licensed Estate Agent / Partner</p>
      <ul class="contact-list">
        <li>
          <svg viewBox="0 0 16 16" aria-hidden="true"><path d="M3 1h3l1.5 4-2 1.3a9 9 0 0 0 4.2 4.2L11 8.5l4 1.5v3a2 2 0 0 1-2 2A12 12 0 0 1 1 3a2 2 0 0 1 2-2z"/></svg>
          +34.611.48.27.09
        </li>
        <li>
          <svg viewBox="0 0 16 16" aria-hidden="true"><path d="M1 3h14v10H1z M1 3l7 6 7-6" stroke="#fff" stroke-width="1"/></svg>
          Ingrid@harbourkeyestates.com
        </li>
        <li>
          <svg viewBox="0 0 16 16" aria-hidden="true"><circle cx="8" cy="8" r="7"/><path d="M1 8h14M8 1c-3 3-3 11 0 14M8 1c3 3 3 11 0 14" stroke="#fff" stroke-width="1" fill="none"/></svg>
          www.harbourkeyestates.com
        </li>
      </ul>
    </div>

    <p class="area-line">Altea-Calpe-Moraira-Javea-Denia-Marina Alta</p>
  </section>

</main>
</body>
</html>
```